Systemischer Coach sucht Flyer-Design
Zielgruppe
Ich bin systemischer Coach und gebe Einzelcoaching in einem sehr schönen Coaching Raum in Aachen.
Meine Zielgruppe sind Menschen im Alter von 28-50, die ehrgeizig, selbstbestimmt und modern sind und sich gerne weiterentwickeln möchten.
Zentrale Themen sind:
Motivation
Persönlichkeitsentwicklung
Ziel- und Entscheidungsfindung
Selbst-/Zeitmanagement
Selbstbewusstsein stärken
Work-Life-Balance
Stressmanagement
Coaching ist professioneller, individueller Begleitprozess für Menschen in herausfordernden Berufs- und Lebenssituationen. Im Rahmen eines systemischen und humanistischen Verständnisses wird der Klient dabei unterstützt, eigenständig konstruktive und nachhaltige Lösungen zu erarbeiten. Das Coaching findet in geschütztem Rahmen statt, Coach und Klient begegnen sich auf Augenhöhe. Der Klient ist Experte für die Inhalte, der Coach ist Experte für Prozess und Struktur
Aufgabenstellung
Farben
schwarz/gold
Vorderseite schlichte/kräftige Symbole und Motto 'Feel the flow'
Rückseite: Text
Text:
'Feel the Flow'
Ist es Zeit,
Deine Stärken zu entdecken?
Deine Ressourcen zu reaktivieren?
Work und Life wieder in Balance zu bringen?
für etwas mehr Motivation und Inspiration?
Suchst Du,
Mut, um Deine Ziele zu erreichen?
Wege, um den Stress links liegen zu lassen?
Selbstbewusstsein für ein sicheres Auftreten?
Struktur und Klarheit im Job?
Bring Flow in Dein Leben!
Als Coach begleite ich Dich auf Deinem Weg zum Ziel

```html
<!DOCTYPE html>
<html lang="de">
<head>
<meta charset="utf-8">
<title>Feel the Flow – Flyer</title>
<link rel="stylesheet" href="https://fonts.googleapis.com/css2?family=Source+Sans+3:ital,wght@0,400;0,700;1,400&display=swap">
<style>
  :root {
    --stage-dark: #3d3d3d;
    --stage-light: #787876;
    --ink: #1d1d1b;
    --paper: #ffffff;
    --frame: #9a9a9a;
    --night: #050508;
    --photo-top: #6f8fa3;
    --photo-mid: #b79a7c;
    --photo-low: #3a3030;
    --accent-pink: #e0288c;
  }
  * { box-sizing: border-box; margin: 0; padding: 0; }
  html, body { width: 1200px; height: 1200px; overflow: hidden; }
  body {
    position: relative;
    font-family: "Source Sans 3", sans-serif;
    background: linear-gradient(90deg, var(--stage-dark) 0%, var(--stage-light) 50%, var(--stage-dark) 100%);
  }
  .flyer-side { position: absolute; left: 173px; width: 858px; overflow: hidden; }

  /* Vorderseite */
  .flyer-front { top: 142px; height: 429px; background: var(--night); }
  .front-photo {
    position: absolute; inset: 0;
    background: linear-gradient(180deg, var(--photo-top) 0%, var(--photo-mid) 40%, var(--photo-low) 68%, var(--night) 84%, var(--night) 100%);
  }
  .front-arrow { position: absolute; inset: 0; }
  .front-motto {
    position: absolute; left: 0; right: 0; top: 330px;
    text-align: center; color: var(--paper);
    font-style: italic; font-weight: 400; font-size: 46px; letter-spacing: -0.5px;
  }

  /* Rückseite */
  .flyer-back {
    top: 633px; height: 432px; background: var(--paper);
    border: 1px solid var(--frame); outline: 1px solid var(--paper); outline-offset: 1px;
  }
  .question-block {
    position: absolute; top: 89px; color: var(--ink);
    font-size: 17.8px; line-height: 23px; letter-spacing: 0.2px;
  }
  .question-block strong { font-weight: 700; }
  .question-block--left { left: 67px; }
  .question-block--right { left: 454px; }
  .back-headline {
    position: absolute; left: 70px; top: 290px;
    font-size: 36.5px; font-weight: 700; color: var(--ink); letter-spacing: 0.2px;
  }
  .back-arrow { position: absolute; inset: 0; }
  .back-closing {
    position: absolute; left: 70px; top: 377px;
    font-size: 18px; color: var(--ink); letter-spacing: 0.2px;
  }
</style>
</head>
<body>

<section class="flyer-side flyer-front">
  <div class="front-photo" role="img" aria-label="Foto: springende Person vor Berglandschaft im Gegenlicht bei Sonnenaufgang"></div>
  <svg class="front-arrow" width="858" height="429" viewBox="0 0 858 429">
    <g fill="none" stroke="#ffffff" stroke-width="1" stroke-linecap="round">
      <path d="M496 327 C 620 338, 720 322, 789 255"/>
      <path d="M789 255 C 780 258, 772 260, 764 261"/>
      <path d="M789 255 C 783 266, 778 278, 776 289"/>
    </g>
  </svg>
  <h1 class="front-motto">Feel the Flow</h1>
</section>

<section class="flyer-side flyer-back">
  <p class="question-block question-block--left">
    <strong>Ist es Zeit</strong>,<br>
    Deine Stärken zu entdecken?<br>
    Deine Ressourcen zu reaktivieren?<br>
    Work und Life wieder in Balance zu bringen?<br>
    für etwas mehr Motivation und Inspiration?
  </p>
  <p class="question-block question-block--right">
    <strong>Suchst Du</strong>,<br>
    Mut, um Deine Ziele zu erreichen?<br>
    Wege, um den Stress links liegen zu lassen?<br>
    Selbstbewusstsein für ein sicheres Auftreten?<br>
    Struktur und Klarheit im Job?
  </p>
  <h2 class="back-headline">Bring Flow in Dein Leben!</h2>
  <svg class="back-arrow" width="858" height="432" viewBox="0 0 858 432">
    <g fill="none" stroke="var(--accent-pink)" stroke-width="1" stroke-linecap="round">
      <path d="M454 353 C 580 366, 690 350, 749 283"/>
      <path d="M749 283 C 740 289, 731 291, 722 291"/>
      <path d="M749 283 C 742 294, 738 306, 736 318"/>
    </g>
  </svg>
  <p class="back-closing">Als Coach begleite ich Dich auf Deinem Weg zum Ziel</p>
</section>

</body>
</html>
```